A website for Veltranor Limited

We need a new and modern website for our company. We are engineering consultants and contractors (EPC) in the oil and gas industry and building services industry.
What we do:
Engineering, procurement, construction
Automation (safety and process)
Non-destructive testing
Training
We have an existing website and the content can be referred from there since we are remaking the website
For more information visit Veltranor Limited Kenya

```html
<!DOCTYPE html>
<html lang="en">
<head>
<meta charset="utf-8">
<title>Veltranor Limited — Engineering Consultants and Contractors</title>
<link rel="stylesheet" href="https://fonts.googleapis.com/css2?family=Domine:wght@400;500;600;700&family=Noto+Serif:wght@400;700&display=swap">
<style>
:root{
  --orange:#f06a23;
  --ink:#111111;
  --text:#3a3a3a;
  --muted:#555;
  --paper:#ffffff;
  --mist:#f1f0f1;
  --night:#000000;
  --white:#ffffff;
}
*{box-sizing:border-box;margin:0;padding:0}
html,body{width:1200px;height:4073px;overflow:hidden;background:var(--paper)}
body{position:relative;font-family:"Noto Serif",Georgia,serif;color:var(--text)}
.abs{position:absolute}
.display{font-family:"Domine",Georgia,serif;font-weight:700}
.heading{font-family:"Domine",Georgia,serif;color:var(--ink);font-weight:700}

/* header & hero */
.hero{left:0;top:0;width:1200px;height:708px;
  background:linear-gradient(90deg,rgba(20,24,34,.88) 0%,rgba(40,44,56,.65) 45%,rgba(70,76,88,.35) 100%),
  linear-gradient(180deg,#5d6472 0%,#3f4654 40%,#2d313b 100%)}
.brand{left:134px;top:44px;color:var(--white);font-family:"Domine",Georgia,serif;font-weight:700;font-size:22px;letter-spacing:.5px;line-height:1}
.nav{left:389px;top:46px;display:flex;gap:35px;color:var(--white);font-size:15px}
.phone{left:965px;top:40px;display:flex;align-items:center;gap:16px;color:var(--white);font-size:15px}
.icon-dot{width:32px;height:32px;border-radius:50%;background:var(--orange);display:flex;align-items:center;justify-content:center}
.hero-title{left:149px;top:292px;color:var(--white);font-size:42px;letter-spacing:.5px}
.hero-sub{left:150px;top:346px;color:var(--white);font-family:"Domine",Georgia,serif;font-weight:700;font-size:28px;line-height:1.08}
.btn{background:var(--orange);color:var(--white);font-family:"Domine",Georgia,serif;font-weight:700;text-transform:uppercase;display:flex;align-items:center;justify-content:center}
.hero-btn{left:149px;top:433px;width:161px;height:46px;font-size:15px}

/* who we are */
.who-bg{left:0;top:708px;width:1200px;height:604px}
.who-title{left:617px;top:833px;font-size:40px}
.rule{height:4px;background:var(--orange)}
.who-copy{left:617px;top:918px;width:470px;font-size:17.5px;line-height:25px;color:var(--text)}
.who-lead{left:617px;top:1070px;width:480px;font-family:"Domine",Georgia,serif;font-weight:600;font-size:21px;line-height:25px;color:var(--ink)}

/* what we do */
.wwd-title{left:0;width:1200px;top:1367px;text-align:center;font-size:40px}
.wwd-intro{left:230px;width:740px;top:1456px;text-align:center;font-size:17.5px;line-height:25px;color:var(--text)}
.frame{border:2px solid var(--orange)}
.photo{position:absolute}
.svc-title{font-family:"Domine",Georgia,serif;font-weight:500;font-size:23px;color:var(--ink)}
.svc-body{font-size:13.3px;line-height:19px;color:var(--muted);width:490px;margin-top:16px}
.svc-btn-wrap{position:relative;width:146px;height:50px;margin-top:27px}
.svc-btn-wrap .outline{position:absolute;left:7px;top:7px;width:139px;height:43px;border:2px solid var(--orange)}
.svc-btn-wrap .btn{position:absolute;left:0;top:0;width:139px;height:43px;font-size:13.5px}

/* contact */
.road{left:0;top:3083px;width:1200px;height:634px;background:linear-gradient(180deg,#ffffff 0%,#e6e6e8 30%,#b9babd 65%,#9d9ea2 100%)}
.contact-card{left:175px;top:3143px;width:849px;height:458px;background:var(--orange);opacity:.96}
.contact-title{left:0;width:1200px;top:3208px;text-align:center;color:var(--white);font-family:"Domine",Georgia,serif;font-weight:700;font-size:38px}
.field{color:var(--white)}
.field .label{font-family:"Domine",Georgia,serif;font-weight:700;font-size:15px}
.field .hint{font-size:10px;opacity:.85;margin-top:6px}
.field .line{height:1.5px;background:var(--white);opacity:.85;margin-top:4px}
.submit{left:519px;top:3575px;width:162px;height:52px;background:var(--night);color:var(--white);font-family:"Domine",Georgia,serif;font-weight:700;font-size:19px;display:flex;align-items:center;justify-content:center}

/* footer */
.footer{left:0;top:3717px;width:1200px;height:356px;background:var(--night)}
.foot-nav{left:0;width:1200px;top:3828px;display:flex;justify-content:center;gap:39px;color:var(--white);font-family:"Domine",Georgia,serif;font-weight:600;font-size:16px}
.foot-info{display:flex;gap:12px;color:var(--white);font-family:"Domine",Georgia,serif;font-weight:700;font-size:14px;line-height:18px}
.foot-rule{left:202px;top:3995px;width:796px;height:1px;background:#444}
.copy{left:0;width:1200px;top:4015px;text-align:center;color:var(--white);font-size:14px}
</style>
</head>
<body>

<!-- Hero -->
<section class="abs hero" role="img" aria-label="Photo of an engineer in hard hat and safety vest holding plans above a construction site"></section>
<div class="abs brand">VELTRANOR LIMITED</div>
<nav class="abs nav"><span>Home</span><span>About Us</span><span>What we do</span><span>Team</span><span>Projects</span><span>Contact</span></nav>
<div class="abs phone">
  <span class="icon-dot"><svg width="16" height="16" viewBox="0 0 24 24"><path fill="#fff" d="M6.6 10.8c1.4 2.8 3.8 5.1 6.6 6.6l2.2-2.2c.3-.3.7-.4 1-.2 1.1.4 2.3.6 3.6.6.6 0 1 .4 1 1V20c0 .6-.4 1-1 1C10.6 21 3 13.4 3 4c0-.6.4-1 1-1h3.5c.6 0 1 .4 1 1 0 1.3.2 2.5.6 3.6.1.3 0 .7-.2 1z"/></svg></span>
  <span>(123) 555 0147</span>
</div>
<h1 class="abs display hero-title">VELTRANOR LIMITED</h1>
<p class="abs hero-sub">We are engineering consultants<br>and contractors</p>
<a class="abs btn hero-btn">Learn More</a>

<!-- Who we are -->
<svg class="abs who-bg" width="1200" height="604" viewBox="0 0 1200 604">
  <defs>
    <linearGradient id="whoPhoto" x1="0" y1="0" x2="1" y2="0">
      <stop offset="0" stop-color="#5e6f86"/>
      <stop offset="0.45" stop-color="#9aa3b2"/>
      <stop offset="0.75" stop-color="#f0955e"/>
      <stop offset="1" stop-color="#f1f0f1"/>
    </linearGradient>
  </defs>
  <polygon points="0,0 1200,0 1200,604 0,510" fill="#f1f0f1"/>
  <polygon points="0,0 640,0 640,556 0,510" fill="url(#whoPhoto)" role="img" aria-label="Double exposure of an engineer in a hard hat blended with a city skyline at sunset"/>
</svg>
<h2 class="abs heading who-title">WHO WE ARE</h2>
<div class="abs rule" style="left:617px;top:886px;width:100px"></div>
<p class="abs who-copy">Lorem ipsum dolor sit amet, consectetur adipiscing elit, sed do eiusmod tempor incididunt ut labore et dolore magna aliqua. Quis ipsum suspendisse ultrices gravida. Risus commodo viverra maecenas accumsan lacus vel facilisis.</p>
<p class="abs who-lead">We are engineering consultants and contractors (EPC) in the oil and gas industry and building services industry.</p>

<!-- What we do -->
<h2 class="abs heading wwd-title">WHAT WE DO</h2>
<div class="abs rule" style="left:550px;top:1420px;width:100px"></div>
<p class="abs wwd-intro">Lorem ipsum dolor sit amet, consectetur adipiscing elit, sed do eiusmod tempor incididunt ut labore et dolore magna aliqua. Quis ipsum suspendisse ultrices gravida. Risus commodo viverra maecenas accumsan lacus vel facilisis.</p>

<!-- Service 1 -->
<div class="abs frame" style="left:166px;top:1579px;width:321px;height:239px"></div>
<div class="photo" style="left:185px;top:1598px;width:346px;height:267px;background:linear-gradient(160deg,#6b4a3a 0%,#c9672b 45%,#f2a14a 60%,#2a2220 100%)" role="img" aria-label="Excavator and workers silhouetted against a sunset construction site"></div>
<div class="abs" style="left:561px;top:1626px">
  <h3 class="svc-title">Engineering, procurement, construction</h3>
  <p class="svc-body">Lorem ipsum dolor sit amet, consectetur adipiscing elit, sed do eiusmod tempor incididunt ut labore et dolore magna aliqua. Quis ipsum suspen disse ultrices gravida. Risus commodo viverra maecenas accumsan lacus vel facilisis. e et dolore magna aliqua. Quis ipsum suspen disse ultrices gravidsus commodo viverra maecenas accumsa</p>
  <div class="svc-btn-wrap"><span class="outline"></span><a class="btn">Learn More</a></div>
</div>

<!-- Service 2 -->
<div class="abs frame" style="left:707px;top:1954px;width:322px;height:240px"></div>
<div class="photo" style="left:666px;top:1973px;width:346px;height:267px;background:linear-gradient(135deg,#1f3f4a 0%,#2f5d66 45%,#c4683f 75%,#1a2a30 100%)" role="img" aria-label="Engineer in hard hat operating an industrial control touchscreen"></div>
<div class="abs" style="left:149px;top:2001px">
  <h3 class="svc-title">Automation (safety and process)</h3>
  <p class="svc-body">Lorem ipsum dolor sit amet, consectetur adipiscing elit, sed do eiusmod tempor incididunt ut labore et dolore magna aliqua. Quis ipsum suspen disse ultrices gravida. Risus commodo viverra maecenas accumsan lacus vel facilisis. e et dolore magna aliqua. Quis ipsum suspen disse ultrices gravidsus commodo viverra maecenas accumsa</p>
  <div class="svc-btn-wrap"><span class="outline"></span><a class="btn">Learn More</a></div>
</div>

<!-- Service 3 -->
<div class="abs frame" style="left:166px;top:2326px;width:321px;height:239px"></div>
<div class="photo" style="left:185px;top:2345px;width:346px;height:267px;background:linear-gradient(150deg,#3a3a3c 0%,#c9c9c9 35%,#efefef 60%,#6b6461 100%)" role="img" aria-label="Hands reviewing technical plans with a calculator on a desk"></div>
<div class="abs" style="left:561px;top:2372px">
  <h3 class="svc-title">Non-destructive testing</h3>
  <p class="svc-body">Lorem ipsum dolor sit amet, consectetur adipiscing elit, sed do eiusmod tempor incididunt ut labore et dolore magna aliqua. Quis ipsum suspen disse ultrices gravida. Risus commodo viverra maecenas accumsan lacus vel facilisis. e et dolore magna aliqua. Quis ipsum suspen disse ultrices gravidsus commodo viverra maecenas accumsa</p>
  <div class="svc-btn-wrap"><span class="outline"></span><a class="btn">Learn More</a></div>
</div>

<!-- Service 4 -->
<div class="abs frame" style="left:707px;top:2700px;width:322px;height:240px"></div>
<div class="photo" style="left:666px;top:2719px;width:346px;height:267px;background:linear-gradient(160deg,#8a8f96 0%,#c7c9cc 35%,#e8843c 65%,#5a4a40 100%)" role="img" aria-label="Three workers in hard hats and safety vests reviewing plans on site"></div>
<div class="abs" style="left:149px;top:2747px">
  <h3 class="svc-title">Training</h3>
  <p class="svc-body">Lorem ipsum dolor sit amet, consectetur adipiscing elit, sed do eiusmod tempor incididunt ut labore et dolore magna aliqua. Quis ipsum suspen disse ultrices gravida. Risus commodo viverra maecenas accumsan lacus vel facilisis. e et dolore magna aliqua. Quis ipsum suspen disse ultrices gravidsus commodo viverra maecenas accumsa</p>
  <div class="svc-btn-wrap"><span class="outline"></span><a class="btn">Learn More</a></div>
</div>

<!-- Contact -->
<div class="abs road" role="img" aria-label="Misty open highway stretching into the distance"></div>
<div class="abs contact-card"></div>
<h2 class="abs display contact-title">Contact Us</h2>
<div class="abs field" style="left:270px;top:3314px;width:326px"><div class="label">Your Name</div><div class="hint">Alex</div><div class="line"></div></div>
<div class="abs field" style="left:617px;top:3314px;width:325px"><div class="label">Company Name</div><div class="hint">Company Name</div><div class="line"></div></div>
<div class="abs field" style="left:270px;top:3389px;width:326px"><div class="label">Email</div><div class="hint">alex@mailbox.com</div><div class="line"></div></div>
<div class="abs field" style="left:617px;top:3389px;width:325px"><div class="label">Phone</div><div class="hint">xxxxxxxx89</div><div class="line"></div></div>
<div class="abs field" style="left:270px;top:3458px;width:675px"><div class="label">Message</div><div class="hint">Type Message</div><div class="line" style="margin-top:34px"></div></div>
<a class="abs submit">SUBMIT</a>

<!-- Footer -->
<footer class="abs footer"></footer>
<nav class="abs foot-nav"><span>Home</span><span>About Us</span><span>What we do</span><span>Team</span><span>Projects</span><span>Contact</span></nav>
<div class="abs foot-info" style="left:274px;top:3912px">
  <svg width="22" height="18" viewBox="0 0 24 20" style="margin-top:6px"><rect x="1" y="2" width="22" height="16" rx="2" fill="#f06a23"/><path d="M2 4l10 7 10-7" stroke="#000" stroke-width="2" fill="none"/></svg>
  <div>Email:<br>info@veltranorlimited.com</div>
</div>
<div class="abs foot-info" style="left:557px;top:3912px">
  <svg width="22" height="22" viewBox="0 0 24 24" style="margin-top:3px"><path fill="#f06a23" d="M6.6 10.8c1.4 2.8 3.8 5.1 6.6 6.6l2.2-2.2c.3-.3.7-.4 1-.2 1.1.4 2.3.6 3.6.6.6 0 1 .4 1 1V20c0 .6-.4 1-1 1C10.6 21 3 13.4 3 4c0-.6.4-1 1-1h3.5c.6 0 1 .4 1 1 0 1.3.2 2.5.6 3.6.1.3 0 .7-.2 1z"/></svg>
  <div>Phone:<br>989 xx x4210</div>
</div>
<div class="abs foot-info" style="left:740px;top:3912px">
  <svg width="18" height="24" viewBox="0 0 18 24" style="margin-top:2px"><path fill="#f06a23" d="M9 0C4 0 0 4 0 9c0 6.5 9 15 9 15s9-8.5 9-15c0-5-4-9-9-9zm0 12.5A3.5 3.5 0 1 1 9 5.5a3.5 3.5 0 0 1 0 7z"/></svg>
  <div>Address:<br>Lorem dumy text 098</div>
</div>
<div class="abs foot-rule"></div>
<p class="abs copy">©2023 Veltranor Limited. All rights are reserved.</p>

</body>
</html>
```